Norwell Asset Partners, LLC

I need a new business card desperately.

Please update my business card. I am looking for a professional modern classy design like the Brisket Holdings card in the attachments.

Industry/Entity Type

Investment

Contact Information for Business Card

Colors

Designer to choose colors to be used in the design.

```html
<!DOCTYPE html>
<html lang="en">
<head>
<meta charset="utf-8">
<title>Norwell Asset Partners, LLC — Business Card</title>
<link rel="stylesheet" href="https://fonts.googleapis.com/css2?family=Lato:wght@300;400;700;900&display=swap">
<style>
  :root {
    --navy: #0f4a63;
    --gold: #d1a75e;
    --paper: #ffffff;
    --backdrop: #e9ebee;
    --ghost: #f2f3f5;
    --ink-soft: #2d5468;
  }
  * { box-sizing: border-box; margin: 0; padding: 0; }
  html, body { width: 1200px; height: 880px; overflow: hidden; }
  body {
    background: var(--backdrop);
    font-family: "Lato", sans-serif;
    position: relative;
  }
  .card {
    position: absolute;
    width: 620px;
    height: 354px;
    border-radius: 22px;
    overflow: hidden;
    box-shadow: 0 14px 34px rgba(0, 0, 0, 0.18);
  }

  /* Back side */
  .card--back {
    left: 80px;
    top: 60px;
    background: var(--navy);
    display: flex;
    align-items: center;
    justify-content: center;
  }
  .brand {
    display: flex;
    align-items: center;
    gap: 14px;
    font-family: "Lato", sans-serif;
    font-weight: 700;
    letter-spacing: 0.08em;
    text-transform: uppercase;
  }
  .brand__mark { width: 22px; height: 22px; flex: none; }
  .card--back .brand { color: var(--gold); font-size: 24px; }
  .card--back .brand__mark { background: var(--gold); }

  /* Front side */
  .card--front {
    left: 500px;
    top: 470px;
    background: var(--paper);
  }
  .front__ghost {
    position: absolute;
    right: 50px;
    top: 24px;
    width: 200px;
    height: 160px;
    background: var(--ghost);
  }
  .card--front .brand {
    position: absolute;
    left: 40px;
    top: 52px;
    color: var(--navy);
    font-size: 19px;
  }
  .card--front .brand__mark { background: var(--navy); width: 18px; height: 18px; }
  .front__rule {
    position: absolute;
    left: 150px;
    right: 28px;
    top: 200px;
    height: 2px;
    background: var(--gold);
  }
  .person {
    position: absolute;
    left: 40px;
    top: 160px;
  }
  .person__name {
    font-size: 22px;
    color: var(--navy);
    line-height: 1;
    letter-spacing: 0.01em;
  }
  .person__first { font-weight: 900; }
  .person__last { font-weight: 300; }
  .person__role {
    color: var(--gold);
    font-size: 16px;
    font-weight: 400;
    margin-top: 2px;
  }
  .contact {
    position: absolute;
    left: 40px;
    top: 230px;
    list-style: none;
    font-size: 15px;
    color: var(--navy);
  }
  .contact li {
    display: flex;
    align-items: center;
    gap: 10px;
    height: 24px;
  }
  .contact svg { width: 18px; height: 18px; flex: none; }
  .address {
    position: absolute;
    right: 28px;
    top: 212px;
    text-align: right;
    font-size: 14px;
    line-height: 1.35;
    color: var(--navy);
  }
  .band-gold {
    position: absolute;
    left: 0;
    bottom: 0;
    width: 392px;
    height: 12px;
    background: var(--gold);
  }
  .band-navy {
    position: absolute;
    right: 0;
    bottom: 0;
    width: 236px;
    height: 80px;
    background: var(--navy);
  }
</style>
</head>
<body>

  <section class="card card--back" aria-label="Card back">
    <div class="brand">
      <span class="brand__mark"></span>
      <span class="brand__name">Norwell Asset Partners, LLC</span>
    </div>
  </section>

  <section class="card card--front" aria-label="Card front">
    <div class="front__ghost" role="img" aria-label="Faint brand decoration"></div>

    <div class="brand">
      <span class="brand__mark"></span>
      <span class="brand__name">Norwell Asset Partners, LLC</span>
    </div>

    <div class="front__rule"></div>

    <div class="person">
      <p class="person__name"><span class="person__first">OWEN</span> <span class="person__last">HARTLEY</span></p>
      <p class="person__role">Owner</p>
    </div>

    <ul class="contact">
      <li>
        <svg viewBox="0 0 18 18" aria-hidden="true"><circle cx="9" cy="9" r="9" fill="var(--gold)"/><rect x="6" y="4" width="6" height="10" rx="1.2" fill="none" stroke="#fff" stroke-width="1.3"/></svg>
        <span>(555) 210-4477</span>
      </li>
      <li>
        <svg viewBox="0 0 18 18" aria-hidden="true"><circle cx="9" cy="9" r="9" fill="var(--gold)"/><rect x="4.5" y="5.8" width="9" height="6.4" fill="none" stroke="#fff" stroke-width="1.2"/><path d="M4.5 6 9 9.6 13.5 6" fill="none" stroke="#fff" stroke-width="1.2"/></svg>
        <span>hello@norwellasset.com</span>
      </li>
      <li>
        <svg viewBox="0 0 18 18" aria-hidden="true"><circle cx="9" cy="9" r="9" fill="var(--gold)"/><circle cx="9" cy="9" r="4.6" fill="none" stroke="#fff" stroke-width="1.1"/><path d="M4.4 9h9.2M9 4.4c-2.4 2.6-2.4 6.6 0 9.2M9 4.4c2.4 2.6 2.4 6.6 0 9.2" fill="none" stroke="#fff" stroke-width="1"/></svg>
        <span>www.norwellasset.com</span>
      </li>
    </ul>

    <address class="address" style="font-style:normal">
      PO Box 48 Harbor Rd,<br>9 Elm Street, Norwell, USA
    </address>

    <div class="band-gold"></div>
    <div class="band-navy"></div>
  </section>

</body>
</html>
```